Marta Quinlan Photography needs a unique, creative business card/logo design

I need a design for business cards/logo that is unique and creative in the industry. Simplicity is nice, so not too crowded. Something that will catch my customer's eye and remain in their memory. I am primarily a landscape photographer but will be soon may be branching into boudoir photography as well. I have attached my current card.

Industry/Entity Type

Business

Contact Information for Business Card

Marta Quinlan Photography
Phone: 0439 271 504
Email: MartaQuinlanPhotography@brivomail.net
Website: www.pagerly.net/MartaQuinlanPhotography.Aust

Logo Text

Marta Quinlan Photography

Requirements
Must have
• Contact Details on one side
Should not have
• pixelation

```html
<!DOCTYPE html>
<html lang="en">
<head>
<meta charset="utf-8">
<title>Marta Quinlan Photography — Business Card</title>
<link rel="stylesheet" href="https://fonts.googleapis.com/css2?family=Open+Sans:wght@400;600&family=Josefin+Sans:wght@300&display=swap">
<style>
  :root {
    --backdrop: #4a3b2e;
    --card-light: #ffffff;
    --card-dark: #262424;
    --ink-dark: #231f20;
    --ink-light: #e9e7e4;
    --contact-ink: #3a3738;
  }
  html, body {
    margin: 0;
    padding: 0;
    width: 1200px;
    height: 750px;
    overflow: hidden;
    background: var(--backdrop);
  }
  .canvas {
    position: relative;
    width: 1200px;
    height: 750px;
  }
  .card {
    position: absolute;
    top: 228px;
    width: 462px;
    height: 263px;
    overflow: hidden;
  }
  .card--front {
    left: 135px;
    background: var(--card-light);
  }
  .card--back {
    left: 616px;
    background: var(--card-dark);
  }
  .brand-disc {
    position: absolute;
    width: 262px;
    height: 262px;
    border-radius: 50%;
    top: 1px;
  }
  .card--front .brand-disc {
    right: -131px;
    background: var(--ink-dark);
  }
  .card--back .brand-disc {
    left: -131px;
    background: var(--card-light);
  }
  .contact-block {
    position: absolute;
    left: 40px;
    top: 88px;
    font-family: "Open Sans", Arial, sans-serif;
    color: var(--ink-dark);
  }
  .contact-name {
    margin: 0 0 10px;
    font-size: 17.5px;
    font-weight: 600;
    letter-spacing: -0.2px;
  }
  .contact-list {
    list-style: none;
    margin: 0;
    padding: 0;
  }
  .contact-item {
    display: flex;
    align-items: center;
    height: 17.5px;
    font-size: 12.4px;
    color: var(--contact-ink);
  }
  .contact-icon {
    width: 12px;
    height: 12px;
    margin-right: 8px;
    flex: none;
  }
  .wordmark {
    position: absolute;
    left: 190px;
    top: 98px;
    width: 240px;
    text-align: center;
    font-family: "Josefin Sans", "Century Gothic", sans-serif;
    font-weight: 300;
    color: var(--ink-light);
    text-transform: uppercase;
  }
  .wordmark-name,
  .wordmark-trade {
    margin: 0;
    font-size: 17px;
    letter-spacing: 5.4px;
    line-height: 32px;
  }
</style>
</head>
<body>
<main class="canvas">

  <section class="card card--front" aria-label="Business card front">
    <div class="contact-block">
      <h1 class="contact-name">MARTA QUINLAN</h1>
      <ul class="contact-list">
        <li class="contact-item">
          <svg class="contact-icon" viewBox="0 0 12 12" aria-hidden="true">
            <rect x="2.5" y="0.5" width="7" height="11" rx="1.2" fill="none" stroke="currentColor" stroke-width="1.3"/>
            <rect x="4" y="2" width="4" height="6.5" fill="currentColor"/>
          </svg>
          <span>0439 271 504</span>
        </li>
        <li class="contact-item">
          <svg class="contact-icon" viewBox="0 0 12 12" aria-hidden="true">
            <rect x="0.5" y="2.5" width="11" height="7.5" fill="currentColor"/>
            <path d="M0.8 2.9 L6 7 L11.2 2.9" fill="none" stroke="#fff" stroke-width="1"/>
          </svg>
          <span>MartaQuinlanPhotography@brivomail.net</span>
        </li>
        <li class="contact-item">
          <svg class="contact-icon" viewBox="0 0 12 12" aria-hidden="true">
            <rect x="1" y="1" width="10" height="10" fill="currentColor"/>
          </svg>
          <span>MartaQuinlanPhotography.Aust</span>
        </li>
      </ul>
    </div>
    <div class="brand-disc" aria-hidden="true"></div>
  </section>

  <section class="card card--back" aria-label="Business card back">
    <div class="brand-disc" aria-hidden="true"></div>
    <div class="wordmark">
      <p class="wordmark-name">Marta Quinlan</p>
      <p class="wordmark-trade">Photography</p>
    </div>
  </section>

</main>
</body>
</html>
```